New business blog needs wordpress theme

I need a unique wordpress theme for my new business oriented blog at quietharlow.net. The blog focuses on my experience as an entrepreneur and offers insights into business problems while chronicling my experience building a new company.

I would like to see a theme that looks more like a creative professional's website, not a business website. Large photos, bright colors, unique layout. I do not want stock photos of people in suits doing business type things. Also, no pictures of me - I am blogging anonymously.

The design should communicate technology and beauty - for example, I really like the feel of the landing page at www.pebblyn.net - it is beautiful to look at but also reflects the cutting edge nature of what they are doing.

Industry/Entity Type

Business

```html
<!DOCTYPE html>
<html lang="en">
<head>
<meta charset="utf-8">
<title>Quiet Harlow</title>
<link rel="stylesheet" href="https://fonts.googleapis.com/css2?family=Ubuntu:wght@400;500;700&family=Arimo:wght@400;700&display=swap">
<style>
:root{
  --ink:#222;
  --muted:#777;
  --body:#7a7a7a;
  --link:#0a35c0;
  --meta-link:#3a6bd0;
  --nav-top:#3a3a3a;
  --nav-bottom:#1c1c1c;
  --nav-line:#4a4a4a;
  --panel-line:#e2e2e2;
  --widget-top:#ffffff;
  --widget-bottom:#f1f1f1;
  --footer:#ececec;
  --rule:#e6e6e6;
  --dot:#8fa4e0;
}
*{box-sizing:border-box;margin:0;padding:0}
html,body{width:1200px;height:2242px;overflow:hidden;background:#fff}
body{position:relative;font-family:"Arimo",Arial,sans-serif;color:var(--ink)}
a{text-decoration:none;color:inherit}

.site-title{position:absolute;left:130px;top:24px;font-family:"Ubuntu",sans-serif;font-weight:700;font-size:29px;color:var(--ink)}
.site-tagline{position:absolute;left:131px;top:71px;font-family:"Ubuntu",sans-serif;font-size:13px;color:var(--muted)}

.main-nav{position:absolute;left:0;top:103px;width:1200px;height:48px;background:linear-gradient(var(--nav-top),var(--nav-bottom));border-bottom:1px solid #111}
.main-nav ul{list-style:none;display:flex;position:absolute;left:130px;top:0;height:48px;border-left:1px solid var(--nav-line)}
.main-nav li{height:48px;line-height:48px;padding:0 22px;font-size:15px;color:#fff;border-right:1px solid var(--nav-line)}

.content-panel{position:absolute;left:131px;top:185px;width:939px;height:1886px;border:1px solid var(--panel-line)}

.post{position:absolute;left:158px;width:601px}
.post-title{font-size:22.5px;line-height:35px;font-weight:400;color:var(--link)}
.post-image{position:absolute;left:0;width:601px;height:283px}
.post-meta{position:absolute;left:2px;font-size:12.5px;color:#444}
.post-meta a{color:var(--meta-link)}
.post-meta .sep{display:inline-block;width:12px}
.post-excerpt{position:absolute;left:0;width:601px;font-size:11.6px;line-height:21.8px;color:var(--body)}
.post-excerpt p+p{margin-top:3px}
.share-row{position:absolute;left:0;width:601px;height:18px}
.share{position:absolute;top:0;display:flex;align-items:center;gap:4px;font-size:10px}
.share .btn{height:16px;padding:0 5px;line-height:14px;border:1px solid #bbb;border-radius:3px;background:linear-gradient(#fff,#e6e6e6);font-weight:700;color:#333}
.share .count{height:16px;min-width:15px;padding:0 3px;line-height:14px;text-align:center;border:1px solid #bbb;border-radius:2px;background:#fff;color:#333}
.share.comments{color:var(--muted);font-size:11px;gap:5px}
.post-rule{position:absolute;left:0;width:601px;height:1px;background:var(--rule)}

.pagination{position:absolute;left:323px;top:2008px;display:flex;gap:4px}
.pagination span{width:19px;height:19px;border:1px solid #ccc;border-radius:50%;font-size:9px;line-height:17px;text-align:center;color:#888}
.pagination .current{background:#222;border-color:#222;color:#fff;font-weight:700}

.sidebar{position:absolute;left:820px;width:220px}
.search-widget{top:215px;height:57px;background:#2b2b2b;padding:17px 18px}
.search-field{position:relative;height:22px;background:#fff;border-radius:11px;font-size:9.5px;color:#aaa;line-height:22px;padding-left:12px}
.search-field svg{position:absolute;right:8px;top:5px}
.widget{border:1px solid #ddd;background:linear-gradient(var(--widget-top),var(--widget-bottom));padding:0 10px}
.widget-title{font-size:18.5px;font-weight:400;text-align:center;color:var(--ink);padding:10px 0 8px;border-bottom:1px solid #ddd;margin:0 5px}
.widget ul{list-style:none;padding:12px 0 0 0}
.widget li{position:relative;padding:0 0 10px 12px;font-size:12.4px;line-height:21px;color:var(--link)}
.widget li::before{content:"\2713";position:absolute;left:1px;top:0;font-size:8px;color:#888}
.widget li+li{border-top:1px dotted var(--dot);padding-top:10px}
.widget li+li::before{top:10px}
.recent-widget{top:300px;height:262px}
.top-widget{top:592px;height:160px}
.links-widget{top:780px;height:160px}

.site-footer{position:absolute;left:0;top:2104px;width:1200px;height:138px;background:var(--footer)}
.footer-nav{position:absolute;left:0;top:44px;width:1200px;text-align:center;font-size:13px;color:#444}
.footer-nav .slash{margin:0 11px;color:#666}
.copyright{position:absolute;left:0;top:88px;width:1200px;text-align:center;font-size:11px;color:#777}
</style>
</head>
<body>

<header>
  <a class="site-title">Quiet Harlow</a>
  <p class="site-tagline">Harlow talks business. Best practices, articles and tips and about small business in the United States.</p>
</header>

<nav class="main-nav">
  <ul>
    <li>Home</li>
    <li>Small Business</li>
    <li>Technology</li>
    <li>About Harlow</li>
    <li>Contact</li>
  </ul>
</nav>

<div class="content-panel"></div>

<!-- Post 1 -->
<article class="post" style="top:206px">
  <h2 class="post-title">Comparing Direct Mail to Dealwise – By the Numbers</h2>
  <div class="post-image" style="top:48px;background:linear-gradient(120deg,#1f4f9e 0%,#8fb2e4 45%,#2a63b8 70%,#5a8fd6 100%)" role="img" aria-label="Blue-tinted photo of a financial newspaper, a small globe and a keyboard"></div>
  <div class="post-meta" style="top:358px">Posted on <a>March 6, 2014</a><span class="sep"></span>by Harlow</div>
  <div class="post-excerpt" style="top:394px">
    <p>Unhappy with the results of a direct mail (snail mail) campaign, I decided to compare the results to a Dealwise c ampaign. I compared both the cost of the respective campaigns, the revenue generated, the customers acquired and customer retention.</p>
    <p>One of my businesses owns and operates franchised hair salons. We have 15 salons across 2 different brands. The company builds new salons and buys and rehabilitates old salons. One brand is a value focused family salo n, the other is a high-end male oriented barbershop.</p>
  </div>
  <div class="share-row" style="top:550px">
    <div class="share" style="left:0"><span class="btn">Chirp</span><span class="count">0</span></div>
    <div class="share" style="left:139px"><span class="btn">Like</span><span class="count">4</span></div>
    <div class="share" style="left:275px"><span class="btn">Boost</span><span class="count">0</span></div>
    <div class="share" style="left:399px"><span class="btn">Save</span><span class="count">2</span></div>
    <div class="share comments" style="left:553px">1<svg width="14" height="12" viewBox="0 0 14 12"><path d="M1 1h12v7H6l-3 3V8H1z" fill="none" stroke="#999"/></svg></div>
  </div>
  <div class="post-rule" style="top:601px"></div>
</article>

<!-- Post 2 -->
<article class="post" style="top:827px">
  <h2 class="post-title">Finally Dumping Chatloop on Pocket OS – Any Recommendations for an SMS App?</h2>
  <div class="post-image" style="top:85px;background:linear-gradient(110deg,#2e4a5e 0%,#6f8fa3 40%,#c9d8e2 55%,#3d5a70 80%,#22384a 100%)" role="img" aria-label="Photo of a hand touching a glowing envelope icon on a blue digital map background"></div>
  <div class="post-meta" style="top:395px">Posted on <a>March 6, 2014</a><span class="sep"></span>by Harlow</div>
  <div class="post-excerpt" style="top:431px">
    <p>Unhappy with the results of a direct mail (snail mail) campaign, I decided to compare the results to a Dealwise c ampaign. I compared both the cost of the respective campaigns, the revenue generated, the customers acquired and customer retentio</p>
  </div>
  <div class="share-row" style="top:519px">
    <div class="share" style="left:0"><span class="btn">Chirp</span><span class="count">0</span></div>
    <div class="share" style="left:139px"><span class="btn">Like</span><span class="count">4</span></div>
    <div class="share" style="left:275px"><span class="btn">Boost</span><span class="count">0</span></div>
    <div class="share" style="left:399px"><span class="btn">Save</span><span class="count">2</span></div>
    <div class="share comments" style="left:553px">1<svg width="14" height="12" viewBox="0 0 14 12"><path d="M1 1h12v7H6l-3 3V8H1z" fill="none" stroke="#999"/></svg></div>
  </div>
  <div class="post-rule" style="top:573px"></div>
</article>

<!-- Post 3 -->
<article class="post" style="top:1418px">
  <h2 class="post-title">Comparing Direct Mail to Dealwise – By the Numbers</h2>
  <div class="post-image" style="top:54px;background:radial-gradient(ellipse at 50% 20%,#f7a247 0%,#f07f35 55%,#ec7330 100%)" role="img" aria-label="Flat illustration of a figure in a suit surrounded by arrows and communication icons on orange"></div>
  <div class="post-meta" style="top:369px">Posted on <a>March 6, 2014</a><span class="sep"></span>by Harlow</div>
  <div class="post-excerpt" style="top:405px">
    <p>Unhappy with the results of a direct mail (snail mail) campaign, I decided to compare the results to a Dealwise c ampaign. I compared both the cost of the respective campaigns, the revenue generated, the customers acquired and customer retentio</p>
  </div>
  <div class="share-row" style="top:487px">
    <div class="share" style="left:0"><span class="btn">Chirp</span><span class="count">0</span></div>
    <div class="share" style="left:139px"><span class="btn">Like</span><span class="count">4</span></div>
    <div class="share" style="left:275px"><span class="btn">Boost</span><span class="count">0</span></div>
    <div class="share" style="left:399px"><span class="btn">Save</span><span class="count">2</span></div>
    <div class="share comments" style="left:553px">1<svg width="14" height="12" viewBox="0 0 14 12"><path d="M1 1h12v7H6l-3 3V8H1z" fill="none" stroke="#999"/></svg></div>
  </div>
  <div class="post-rule" style="top:554px"></div>
</article>

<nav class="pagination">
  <span>&lt;&lt;</span><span>1</span><span class="current">2</span><span>3</span><span>4</span><span>5</span><span>6</span><span>7</span><span>8</span><span>9</span><span>10</span><span>&gt;&gt;</span>
</nav>

<aside>
  <div class="sidebar search-widget">
    <div class="search-field">Keyword...
      <svg width="12" height="12" viewBox="0 0 12 12"><circle cx="5" cy="5" r="3.5" fill="none" stroke="#666" stroke-width="1.5"/><path d="M7.5 7.5L11 11" stroke="#666" stroke-width="1.5"/></svg>
    </div>
  </div>
  <section class="sidebar widget recent-widget">
    <h3 class="widget-title">Recent Posts</h3>
    <ul>
      <li>Comparing Direct Mail to Dealwise By the Numbers</li>
      <li>Finally Dumping Chatloop on Pocket OS – Any Recommendations for an SMS App?</li>
      <li>The Who &amp; The Why</li>
    </ul>
  </section>
  <section class="sidebar widget top-widget">
    <h3 class="widget-title">Top Posts by Clicks</h3>
    <ul><li>quietharlow.net</li></ul>
  </section>
  <section class="sidebar widget links-widget">
    <h3 class="widget-title">Links</h3>
    <ul><li>RSS Feed</li></ul>
  </section>
</aside>

<footer class="site-footer">
  <nav class="footer-nav">Home<span class="slash">//</span>Small Business<span class="slash">//</span>Technology<span class="slash">//</span>About Harlow<span class="slash">//</span>Contact</nav>
  <p class="copyright">© 2014 Quiet Harlow</p>
</footer>

</body>
</html>
```